Locksmith Services Tri Fold Flyer

We are a security company that provide all forms of security, we are looking to have tri fold flyers created for each service we offer starting with Locksmith Services, I am looking to work with someone who can design the layout and advise where the text would go where the pictures would go etc as well as tweaking our current logo, I am hoping to find someone that I can work with across all marketing materials for the business.

Our company is called Harborline Venture Collective , and the Locksmith side will be Harborline Locksmiths which is why the logo will need tweaking but with the text " Part of the Harborline Venture Collective "

Our Strap Line is " Protecting People, Property & Assets "

```html
<!DOCTYPE html>
<html lang="en">
<head>
<meta charset="utf-8">
<title>Harborline Locksmiths – Tri Fold Flyer</title>
<link rel="stylesheet" href="https://fonts.googleapis.com/css2?family=Cinzel:wght@600&family=Poppins:wght@400;600&display=swap">
<style>
  :root{
    --gold:#c9ad6e;
    --gold-deep:#b8975a;
    --ink:#1d1d1d;
    --paper:#ffffff;
    --stage:#e2e2e2;
    --white:#ffffff;
  }
  *{margin:0;padding:0;box-sizing:border-box}
  html,body{width:864px;height:1200px;overflow:hidden;background:var(--stage)}
  body{position:relative;font-family:'Poppins',sans-serif;color:var(--ink)}
  .spread{position:absolute;left:24px;width:816px;height:560px;background:var(--paper);overflow:hidden;box-shadow:0 4px 14px rgba(0,0,0,.12)}
  .spread--outside{top:30px}
  .spread--inside{top:620px}
  .spread svg.art{position:absolute;left:0;top:0}
  .fold{position:absolute;top:0;width:1px;height:100%;background:rgba(0,0,0,.05)}
  .fold--a{left:272px}.fold--b{left:544px}
  .t{position:absolute}
  .serif{font-family:'Cinzel',serif;font-weight:600;text-transform:uppercase;letter-spacing:.5px}
  .heading-white{color:var(--white);font-size:14px;line-height:1.2}
  .heading-white--small{font-size:12px;line-height:1.25}
  .heading-gold{color:var(--gold);font-size:15px;line-height:1.2}
  .lead-gold{color:var(--gold);font-size:8px;line-height:1.4;text-transform:uppercase;letter-spacing:.3px}
  .body{font-size:8.5px;line-height:1.45}
  .body--white{color:var(--white)}
  .web-address{color:var(--white);font-size:8px;letter-spacing:.5px;text-align:center;white-space:nowrap}
  .brand{display:flex;align-items:center;gap:8px;font-family:'Cinzel',serif;font-weight:600;color:var(--gold);text-transform:uppercase;line-height:1.15}
  .brand-dot{width:12px;height:12px;border-radius:50%;background:var(--gold);flex:none}
  .contact-list{list-style:none;font-size:10px;line-height:1.7;text-align:center}
  .service-label{font-size:7.5px;font-weight:600;color:var(--gold);text-transform:uppercase;margin-top:9px}
  .service-title{font-size:8px;font-weight:600;color:var(--gold);line-height:1.3}
  .features{list-style:none;font-size:7.5px;line-height:1.35}
  .features li{position:relative;padding-left:8px;margin-bottom:7px}
  .features li::before{content:"";position:absolute;left:0;top:4px;width:3px;height:3px;border-radius:50%;background:var(--ink)}
  .features-heading{font-size:13px}
</style>
</head>
<body>

<!-- Outside spread -->
<section class="spread spread--outside">
  <svg class="art" width="816" height="560" viewBox="0 0 816 560">
    <defs>
      <linearGradient id="heroTone" gradientUnits="userSpaceOnUse" x1="0" y1="0" x2="816" y2="0">
        <stop offset="0" stop-color="#8fc75b"/>
        <stop offset=".5" stop-color="#a5d277"/>
        <stop offset=".6" stop-color="#8a8a5a"/>
        <stop offset=".72" stop-color="#6a5534"/>
        <stop offset="1" stop-color="#4a3a24"/>
      </linearGradient>
      <linearGradient id="guardTone" x1="0" y1="0" x2="0" y2="1">
        <stop offset="0" stop-color="#8e8e8e"/>
        <stop offset=".6" stop-color="#6a6a6a"/>
        <stop offset="1" stop-color="#3a3a3a"/>
      </linearGradient>
    </defs>
    <g role="img" aria-label="Photo of a key left in a door lock against a soft green background">
      <rect x="0" y="0" width="600" height="110" fill="url(#heroTone)"/>
      <circle cx="600" cy="40" r="180" fill="url(#heroTone)"/>
    </g>
    <path role="img" aria-label="Black and white photo of a security guard seen from behind" d="M0,110 H262 L205,250 Q165,330 45,330 H0 Z" fill="url(#guardTone)"/>
    <path d="M816,300 V345 H786 Z" fill="var(--gold)"/>
  </svg>
  <div class="fold fold--a"></div><div class="fold fold--b"></div>

  <!-- Panel 1 -->
  <h2 class="t serif heading-white" style="left:20px;top:40px;width:240px">Lorem ipsum dolor sit<br>amet, consectetuer</h2>
  <h3 class="t serif heading-gold" style="left:20px;top:345px">About Us</h3>
  <p class="t lead-gold" style="left:20px;top:368px;width:235px">Lorem ipsum dolor sit amet, consectetuer adipiscing elit, sed diam nonummy nibh euismod tincidunt ut laoreet dolore magna aliquam erat volutpat.</p>
  <p class="t body" style="left:20px;top:420px;width:235px">Ing elit, sed diam nonummy nibh euismod tincidunt ut laoreet dolore magna aliquam erat volutpat. Ut wisi enim ad minim. Lorem ipsum dolor sit amet, consectetuer adipiscing elit, sed diam nonummy nibh euismod tincidunt ut laoreet dolore magna aliquam erat volutpat. Ut wisi enim ad minim veniam.</p>

  <!-- Panel 2 -->
  <h2 class="t serif heading-white heading-white--small" style="left:290px;top:34px;width:200px">Lorem ipsum dolor sit<br>amet, consectetuer<br>adipiscing elit, sed</h2>
  <div class="t" style="left:272px;top:318px;width:272px;text-align:center">
    <h3 class="serif heading-gold" style="margin-bottom:6px">Contact</h3>
    <ul class="contact-list">
      <li>+000 000 000</li>
      <li>info@harborlinelocks.com</li>
      <li>www.harborlinelocks.com</li>
    </ul>
  </div>
  <h2 class="t serif heading-gold" style="left:272px;top:470px;width:272px;text-align:center">Lorem ipsum dolor sit<br>amet, consectetuer</h2>

  <!-- Panel 3 -->
  <p class="t serif web-address" style="left:580px;top:22px;width:180px">www.harborlinelocks.com</p>
  <div class="t brand" style="left:574px;top:232px;width:220px;font-size:15px;justify-content:center">
    <span class="brand-dot"></span><span>Harborline Venture Collective</span>
  </div>
  <h1 class="t serif heading-gold" style="left:560px;top:300px;width:240px;text-align:center;font-size:13px">Protecting People,<br>Property &amp; Assets</h1>
  <p class="t body" style="left:568px;top:340px;width:215px;text-align:center">Lorem ipsum dolor sit amet, consectetuer adipiscing elit, sed diam nonummy nibh euismod tincidunt ut laoreet dolore magna aliquam erat volutpat. Ut wisi enim ad minim.</p>
</section>

<!-- Inside spread -->
<section class="spread spread--inside">
  <svg class="art" width="816" height="560" viewBox="0 0 816 560">
    <defs>
      <linearGradient id="keysTone" x1="0" y1="0" x2="1" y2="1">
        <stop offset="0" stop-color="#151515"/>
        <stop offset=".55" stop-color="#4a4a4a"/>
        <stop offset="1" stop-color="#1c1c1c"/>
      </linearGradient>
      <linearGradient id="lockTone" x1="0" y1="0" x2="1" y2="0">
        <stop offset="0" stop-color="#6a5a4c"/>
        <stop offset=".45" stop-color="#c8c4bc"/>
        <stop offset="1" stop-color="#3a2e26"/>
      </linearGradient>
    </defs>
    <g role="img" aria-label="Black and white close-up photo of a bunch of keys">
      <rect x="0" y="0" width="340" height="250" fill="url(#keysTone)"/>
      <circle cx="340" cy="110" r="140" fill="url(#keysTone)"/>
    </g>
    <path d="M0,275 Q40,225 140,225 H272 V560 H0 Z" fill="var(--gold)"/>
    <path role="img" aria-label="Photo of a steel door lock with bolts on a wooden door" d="M575,560 V390 A90,90 0 0 1 665,300 H816 V560 Z" fill="url(#lockTone)"/>
  </svg>
  <div class="fold fold--a"></div><div class="fold fold--b"></div>

  <!-- Panel 1 -->
  <div class="t brand" style="left:20px;top:30px;width:150px;font-size:12px">
    <span class="brand-dot"></span><span>Harborline Venture Collective</span>
  </div>
  <h3 class="t serif heading-white" style="left:20px;top:262px;font-size:15px">How It Works</h3>
  <div class="t body body--white" style="left:20px;top:288px;width:235px">
    <p style="margin-bottom:8px">Lorem ipsum dolor sit amet, consectetuer adipiscing elit, sed diam nonummy nibh euismod tincidunt ut laoreet dolore magna aliquam erat volutpat. Ut wisi enim ad minim veniam, quis nostrud ex</p>
    <p style="margin-bottom:8px">Erci tation ullamcorper suscipit lobortis nisl ut aliquip ex ea commodo consequat. Duis autem vel eum iriure dolor in hendrerit in vulputate velit esse molestie consequat.</p>
    <p style="margin-bottom:8px">Lorem ipsum dolor sit amet, consectetuer adipiscing elit, sed diam nonummy nibh euismod tincidunt ut laoreet dolore magna aliquam erat volutpat. Ut wisi enim ad minim.</p>
    <p>Endrerit in vulputate velit esse molestie consequat, vel illum dolore eu feugiat nulla facilisis at vero eros.</p>
  </div>

  <!-- Panel 2 -->
  <div class="t" style="left:290px;top:272px;width:238px">
    <h3 class="serif heading-gold">Services</h3>
    <p class="service-label">Service 01</p>
    <p class="service-title">Sed diam nonummy nibh euismod tincidunt ut laoreet dolore magna aliquam era</p>
    <p class="body">Erci tation ullamcorper suscipit lobortis nisl ut aliquip ex ea commodo consequat. Duis autem vel eum iriure dolor in hendrerit in vulputate velit esse.</p>
    <p class="service-label">Service 02</p>
    <p class="service-title">Sed diam nonummy nibh euismod tincidunt ut laoreet dolore magna aliquam era</p>
    <p class="body">Erci tation ullamcorper suscipit lobortis nisl ut aliquip ex ea commodo consequat. Duis autem vel eum iriure dolor in hendrerit in vulputate velit esse.</p>
    <p class="service-label">Service 03</p>
    <p class="service-title">Sed diam nonummy nibh euismod tincidunt ut laoreet dolore magna aliquam era</p>
    <p class="body">Erci tation ullamcorper suscipit lobortis nisl ut aliquip ex ea commodo consequat. Duis autem vel eum iriure dolor in hendrerit in vulputate velit esse.</p>
  </div>

  <!-- Panel 3 -->
  <h3 class="t serif heading-gold features-heading" style="left:564px;top:34px">Our Features</h3>
  <ul class="t features" style="left:564px;top:60px;width:112px">
    <li>Lorem ipsum dolor sit amet, consectetuer adipiscing elit, sed diam</li>
    <li>Nonummy nibh euismod tincidunt ut laoreet dolore magna aliquam</li>
    <li>Lorem ipsum dolor sit amet, consectetuer adipiscing elit, sed diam</li>
    <li>Nonummy nibh euismod tincidunt ut laoreet dolore magna aliquam</li>
  </ul>
  <ul class="t features" style="left:696px;top:30px;width:108px">
    <li>Lorem ipsum dolor sit amet, consectetuer adipiscing elit, sed diam</li>
    <li>Nonummy nibh euismod tincidunt ut laoreet dolore magna aliquam</li>
    <li>Lorem ipsum dolor sit amet, consectetuer adipiscing elit, sed diam</li>
    <li>Nonummy nibh euismod tincidunt ut laoreet dolore magna aliquam</li>
  </ul>
</section>

</body>
</html>
```